Flyer-Design für Apotheke
Zielgruppe
Wir sind eine Apotheke, mit Schwerpunkt Mutter-Kind / Wiegenhafen Apotheke (www.wiegenhafen Apotheke)
Zielgruppe: Wir haben uns zertifiziert und spezialisiert im Bereich Mütter / Kinderwunsch / Stillen / Babys etc. (Siehe Anbei unser aktueller Entwurf Mutter-Kind-Broschüre)
Wir haben zahlreiche Handouts zu spezifischen Themen von der LHTV und unserem Verein Wiegenhafen Apotheken für unser Kunden schon fertig gestellt (siehe ein Beispiel im Anhang, auf dem wir noch unser Logo eingefügt haben).
Die Handouts sind meist 4-seitig A5, im Anhang mit unserem Logo noch versehen.
Zu zwei Themen möchten wir jetzt noch selbst ein Handout erstellen.
1) Fieberthermometer
2) Schnuller
Ziel: 4-6 Seiten, wir wollen es dann bei Druckfuchs drucken lassen.
Zielgruppe: Mütter, die zu uns in die Apotheke kommen und beraten werden (konkret in diesen Beispielen zum Thema Fieberthermometer bzw. Schnuller. Damit sie was mit nach Hause nehmen können, möchten wir die Handouts erstellen.
Texte anbei, Graphische Umsetzung ggf. mit netten Baby/Mütterbildern o.ä. erwünscht
Aufgabenstellung
Einbau Logo Tolvena-Apotheke (siehe Anhang) ähnlich wie auf dem Flyer Ernährung
(als Logo ohne Adresse etc. und irgendwo unter mit Adresse, Telefon etc.)
Logo Wiegenhafen Apotheke DARF NICHT MIT DRAUF

```html
<!DOCTYPE html>
<html lang="de">
<head>
<meta charset="utf-8">
<title>Überblick unterschiedliche Messmethoden</title>
<link rel="stylesheet" href="https://fonts.googleapis.com/css2?family=Roboto:wght@400;500;700&display=swap">
<style>
  :root {
    --red: #d0161b;
    --green: #3aa935;
    --text: #3c3c3c;
    --grey-mark: #e3e3e3;
    --frame: #d8d8d8;
    --bug-red: #d9201f;
    --white: #ffffff;
  }
  * { margin: 0; padding: 0; box-sizing: border-box; }
  html, body { width: 1200px; height: 567px; overflow: hidden; background: var(--white); }
  body {
    font-family: "Roboto", Arial, sans-serif;
    color: var(--text);
    font-size: 9.6px;
    line-height: 12.3px;
  }
  .sheet {
    position: relative;
    width: 1200px;
    height: 567px;
    border: 1px solid var(--frame);
    overflow: hidden;
  }
  .title-bar {
    position: absolute;
    left: 0; top: 0;
    width: 400px; height: 56px;
    background: var(--red);
    color: var(--white);
    font-weight: 700;
    font-size: 15.2px;
    line-height: 56px;
    padding-left: 22px;
    padding-top: 2px;
  }
  .block { position: absolute; }
  .method-title { color: var(--red); font-weight: 500; }
  .note-title { font-weight: 500; }
  ul { list-style: none; }
  li { position: relative; padding-left: 8px; }
  li::before { content: "•"; position: absolute; left: 0; }
  li.sub { padding-left: 16px; }
  li.sub::before { left: 8px; }
  .pm { padding-left: 24px; }
  .pm .icon {
    position: absolute; left: 4px; top: 0;
    width: 13.5px; height: 13.5px;
  }
  .mark-bar { position: absolute; background: var(--grey-mark); }
  .bug { position: absolute; }
  .disclaimer { font-size: 6px; line-height: 9.5px; }
</style>
</head>
<body>
<div class="sheet">

  <div class="title-bar">Überblick unterschiedliche Messmethoden:</div>

  <svg width="0" height="0" style="position:absolute">
    <defs>
      <symbol id="icon-plus" viewBox="0 0 20 20">
        <circle cx="10" cy="10" r="10" fill="#3aa935"/>
        <rect x="5" y="8.6" width="10" height="2.8" fill="#fff"/>
        <rect x="8.6" y="5" width="2.8" height="10" fill="#fff"/>
      </symbol>
      <symbol id="icon-minus" viewBox="0 0 20 20">
        <circle cx="10" cy="10" r="10" fill="#d0161b"/>
        <rect x="6" y="8.8" width="8" height="2.4" fill="#fff"/>
      </symbol>
    </defs>
  </svg>

  <!-- Left column -->
  <div class="block" style="left:22px; top:74px; width:352px;">
    <p class="method-title">1. Rektale Messung</p>
    <p>Hierbei wird das Thermometer je nach Produkt 1-3 cm in den After eingeführt und die Temperatur der Schleimhaut gemessen. Je nach Modell erfolgt die Messung innerhalb von wenigen Sekunden durch ein akustisches Signal, verfügt über Mess&shy;wertspeicher, Fieberalarm und beleuchtetem Anzeigefenster.</p>
  </div>

  <div class="block pm" style="left:22px; top:149px; width:352px;">
    <svg class="icon"><use href="#icon-plus"/></svg>
    <p>Vorteil:</p>
    <ul>
      <li>Genauste und zuverlässigste Messung, kommt der Körperkerntemperatur am nächsten</li>
      <li>Für jedes Alter geeignet</li>
      <li>Leichte Reinigung, wasserdicht</li>
    </ul>
  </div>

  <div class="block pm" style="left:22px; top:223px; width:352px;">
    <svg class="icon"><use href="#icon-minus"/></svg>
    <p>Nachteil:</p>
    <ul><li>Unangenehm, von Kindern &amp; Erwachsenen häufig nicht akzeptiert</li></ul>
  </div>

  <div class="block" style="left:22px; top:260px; width:320px;">
    <p class="note-title">Hinweise zur Anwendung:</p>
    <ul>
      <li>Zum leichteren Einführen: Thermometer mit flexibler Spitze verwenden, alternativ mit etwas Vaseline einfetten oder mit Wasser anfeuchten</li>
      <li>Bewährte Messpositionen:</li>
      <li>Babys: auf dem Rücken liegend mit hochgehaltenen Beinchen</li>
      <li>Kleinkinder: mit dem Bauch nach unten über den Schoß</li>
      <li>Ältere Kinder/Erwachsene: Seitenlage mit angezogenen Beinen</li>
    </ul>
  </div>

  <div class="mark-bar" style="left:352px; top:255px; width:19px; height:53px;"></div>
  <div class="mark-bar" style="left:352px; top:320px; width:19px; height:16px;"></div>

  <div class="block" style="left:22px; top:371px; width:352px;">
    <p class="method-title">2. Sublinguale Messung</p>
    <p>Hierbei wird die Temperatur unter der Zunge gemessen.</p>
  </div>

  <div class="block pm" style="left:22px; top:408px; width:352px;">
    <svg class="icon"><use href="#icon-plus"/></svg>
    <p>Vorteil:</p>
    <ul><li>Hohe Akzeptanz</li></ul>
  </div>

  <div class="block pm" style="left:22px; top:446px; width:262px;">
    <svg class="icon"><use href="#icon-minus"/></svg>
    <p>Nachteil:</p>
    <ul>
      <li>Abweichung von der Körperkerntemperatur von -0,3- 0,5°C</li>
      <li>Geeignet ab ca. 4-5 Jahren</li>
      <li>Verfälschungen möglich (geöffneten Mund, Speisen, Getränke, etc.)</li>
    </ul>
  </div>

  <svg class="bug" style="left:292px; top:472px;" width="76" height="62" role="img" aria-label="Illustration eines Marienkäfers">
    <ellipse cx="40" cy="33" rx="30" ry="27" fill="var(--bug-red)"/>
  </svg>

  <!-- Middle column -->
  <div class="block" style="left:420px; top:35px; width:346px;">
    <p class="note-title">Hinweise zur Anwendung:</p>
    <ul>
      <li>Richtige Platzierung der Spitze unter der Zunge, links oder rechts des Zungenbändchens in der dortigen, sogenannten Wärmetasche</li>
      <li>Mund während der Messung schließen und durch die Nase atmen</li>
      <li>Um Verfälschungen zu vermeiden, sollten kalte oder heiße Speisen und Getränke, Rauchen und Kaugummi kauen 10 Minuten vorher unterlassen werden</li>
      <li>Während der Messung darf das Thermometer nicht bewegt werden und der Kontakt zur Schleimhaut muss gegeben sein</li>
    </ul>
  </div>

  <div class="block" style="left:420px; top:159px; width:346px;">
    <p class="method-title">3. Schnullerthermometer</p>
    <p>Dieses Thermometer wird wie ein Schnuller in den Mund des Kindes gesteckt und misst nach ca. 5 Minuten die Temperatur.</p>
  </div>

  <div class="block pm" style="left:420px; top:209px; width:346px;">
    <svg class="icon"><use href="#icon-plus"/></svg>
    <p>Vorteil:</p>
    <ul><li>Evtl. höhere Akzeptanz beim Kind, da es den Schnuller schon kennt</li></ul>
  </div>

  <div class="block pm" style="left:420px; top:245px; width:320px;">
    <svg class="icon"><use href="#icon-minus"/></svg>
    <p>Nachteil:</p>
    <ul>
      <li>Für Kinder bis zu einem Alter von ca. 3 Jahren</li>
      <li>Lange Messdauer</li>
      <li>Verfälschungen möglich (geöffneten Mund v.a. bei verschnupften &amp; weinenden Kindern, Speisen, Getränke)</li>
    </ul>
  </div>

  <div class="block" style="left:420px; top:320px; width:320px;">
    <p class="note-title">Hinweise zur Anwendung:</p>
    <ul>
      <li>Mund während der Messung schließen und durch die Nase atmen</li>
      <li>Um Verfälschungen zu vermeiden, sollten kalte oder heiße Speisen und Getränke 10 Minuten vorher unterlassen werden</li>
    </ul>
  </div>

  <div class="mark-bar" style="left:754px; top:309px; width:19px; height:52px;"></div>
  <div class="mark-bar" style="left:754px; top:374px; width:19px; height:15px;"></div>

  <div class="block" style="left:420px; top:394px; width:346px;">
    <p class="method-title">4. Messung im Ohr</p>
    <p>Hierbei nimmt ein Infrarotsensor im Thermometerkopf die vom Trommelfell ausgehende Wärmestrahlung auf.</p>
  </div>

  <div class="block pm" style="left:418px; top:443px; width:162px; padding-left:21px;">
    <svg class="icon"><use href="#icon-plus"/></svg>
    <p>Vorteil:</p>
    <ul>
      <li>Schnell und präzise</li>
      <li>Für jedes Alter geeignet</li>
      <li>Messung im Schlaf möglich</li>
      <li>hygienisch, da Krankheits&shy;erreger nicht mit dem Thermo&shy;meter in Kontakt kommen</li>
    </ul>
  </div>

  <div class="block pm" style="left:584px; top:443px; width:190px;">
    <svg class="icon"><use href="#icon-minus"/></svg>
    <p>Nachteil:</p>
    <ul>
      <li>Abweichung von der Körperkern&shy;temperatur um -0,5°C</li>
      <li>Verfälschung möglich (Ohrschmalz, sehr enge Gehörgänge)</li>
      <li>Teurer als einfache Thermometer</li>
      <li>Handhabung erfordert gewisse Übung</li>
    </ul>
  </div>

  <!-- Right column -->
  <div class="block" style="left:823px; top:35px; width:351px;">
    <p class="note-title">Hinweise zur Anwendung:</p>
    <ul>
      <li>Bei vorherigen, äußeren Einflüssen (Mütze, auf Ohr gelegen, warm gebadet, etc.) ca. 30 Minuten bis zur Messung abwarten</li>
      <li>Nicht im Ohr messen, wenn davor Ohrentropfen verwendet wurden oder sich Blut bzw. Sekret im Gehörgang befindet</li>
      <li>Bei Entzündungen am äußeren Ohr keine Messung mit dem Ohrthermometer vornehmen</li>
      <li>Handhabung: Damit die Wärmestrahlung den Sensor ungehindert erreicht, muss der natürlich gekrümmte Gehörgang zuvor „begradigt“ werden</li>
      <li class="sub">Kinder bis 1 Jahr: Ohr gerade nach hinten ziehen</li>
      <li class="sub">Kinder ab 1 Jahr: Ohr nach oben und hinten ziehen</li>
    </ul>
  </div>

  <svg class="bug" style="left:1110px; top:163px;" width="62" height="64" role="img" aria-label="Illustration eines Marienkäfers">
    <ellipse cx="30" cy="34" rx="24" ry="24" fill="var(--bug-red)"/>
  </svg>

  <div class="block" style="left:823px; top:196px; width:280px;">
    <p class="method-title">5. Messung an der Stirn</p>
  </div>

  <div class="block pm" style="left:815px; top:213px; width:340px;">
    <svg class="icon"><use href="#icon-plus"/></svg>
    <p>Vorteil:</p>
    <ul>
      <li>Kontaktlos</li>
      <li>Messung im Schlaf möglich</li>
      <li>hygienisch, da Krankheitserreger nicht mit dem Thermometer in Kontakt kommen</li>
      <li>schnelle Messergebnisse</li>
    </ul>
  </div>

  <div class="block pm" style="left:815px; top:300px; width:340px;">
    <svg class="icon"><use href="#icon-minus"/></svg>
    <p>Nachteil:</p>
    <ul>
      <li>Abweichung von der Körperkerntemperatur um -0,5°C</li>
      <li>Geeignet ab ca. 2 Jahren (je nach Modell)</li>
      <li>Stark abhängig von äußeren Einflüssen (Raum- und Hauttemperatur, Verletzungen auf der Haut, etc.)</li>
      <li>Teurer als einfache Thermometer</li>
      <li>Handhabung erfordert gewisse Übung</li>
    </ul>
  </div>

  <div class="block" style="left:823px; top:399px; width:351px;">
    <p class="note-title">Hinweise zur Anwendung:</p>
    <ul>
      <li>Bei vorherigen, äußeren Einflüssen (Mütze, auf Ohr gelegen, warm gebadet, etc.) ca. 30 Minuten bis zur Messung abwarten</li>
      <li>Thermometer muss ebenfalls ca. 30 Minuten in stabiler Umgebungstemperatur gelagert werden</li>
      <li>Haut auf Stirn bzw. Schläfe (je nach Modell) muss trocken und sauber sein, da Feuchtigkeit durch Verdunstungskälte die Messwerte beeinflussen kann</li>
    </ul>
  </div>

  <div class="block disclaimer" style="left:823px; top:524px; width:345px;">
    <p>Die vorliegenden Informationen wurden mit größtmöglicher Sorgfalt nach dem derzeitigen aktuellen Stand der Wissenschaft zusammengestellt, dennoch übernehmen Verfasser und Herausgeber keine Gewähr.</p>
    <p>Es besteht kein Anspruch auf Vollständigkeit.</p>
  </div>

</div>
</body>
</html>
```